Revamp Current Website From 2012 TO 2018

We need a ravamp to our current website. I prefer a professional corporate modern feel to it.

My Current Website is www.brightlanepromoworks.biz. Please redesign the homepage and the /certs page first....see attached document for specific instructions..

There is a lot of content at the bottom but maybe we can shorten that by using titles and a pop up of the details or something so it doesnt take too mcuh space...or maybe a red more hyperlink to see the rest of info in pop up or something or new page...

Target Market(s)

B2B, business owners, website owners, marketing companies.

Industry/Entity Type

Promotional Product

Number of Pages Required

2 page

Colors

Designer to choose colors to be used in the design.

Requirements
Must have
• Please keep in mind logo mock up I am working on that looks beautiful on dark background for header...see attached for logo
• Must use existing content I hope your marketing mind comes in to play when designing the website.
• Must have all my content provided on each page...
Nice to have
• similiar color scheme...
Should not have
• I dont like using templates because usually hard to expand on design in future so Prefer full custom designs
• Please no templates

```html
<!DOCTYPE html>
<html lang="en">
<head>
<meta charset="utf-8">
<title>Bright Lane Promo Works – Unlimited Incentives</title>
<link href="https://fonts.googleapis.com/css2?family=Arimo:wght@400;700&display=swap" rel="stylesheet">
<style>
:root{
  --navy:#1f2a36;
  --nav-active:#ffffff;
  --blue:#1b9ee3;
  --band:#1f9fe0;
  --steel:#5a87a3;
  --red:#e02020;
  --btn-red:#c62a2a;
  --ink:#111111;
  --grey-band:#d6d6d6;
  --footer:#ffffff;
}
*{margin:0;padding:0;box-sizing:border-box}
html,body{width:1200px;height:4737px;overflow:hidden}
body{font-family:"Arimo",Arial,sans-serif;color:var(--ink);background:#fff;position:relative}
.nav{height:54px;background:var(--navy);display:flex;align-items:center;padding-left:14px}
.nav a{color:#fff;text-decoration:none;font-size:19px;padding:0 10px;height:54px;line-height:54px;white-space:nowrap}
.nav a.active{background:var(--nav-active);color:var(--navy)}
.nav a.login{background:#000;height:36px;line-height:36px;margin-left:6px;padding:0 12px}
.header{height:161px;position:relative}
.logo{position:absolute;left:38px;top:38px;display:flex;align-items:center;gap:14px}
.logo-dot{width:86px;height:86px;border-radius:50%;background:#2c3e50}
.logo-name{font-size:64px;font-weight:700;color:#2c3e50;letter-spacing:2px}
.phones{position:absolute;left:478px;top:48px;display:flex;gap:26px;align-items:center}
.phones p{font-size:20px;line-height:27px}
.offer{position:absolute;right:38px;top:34px;text-align:right;font-size:20px;line-height:25px}
.offer strong{font-size:26px;display:block;line-height:32px}
.hero{height:670px;position:relative;background:linear-gradient(100deg,#f3f3f3 0%,#dcdcdc 55%,#b9b9b9 100%)}
.hero-photo{position:absolute;inset:0}
.hero h1{position:absolute;left:41px;top:175px;font-size:54px;line-height:64px;font-weight:700;color:#000}
.btn-red{position:absolute;left:47px;top:418px;width:226px;height:54px;background:var(--btn-red);color:#fff;font-size:20px;display:flex;align-items:center;justify-content:center}
.ways h2{position:absolute;top:970px;left:0;width:100%;text-align:center;font-size:50px;color:var(--blue);font-weight:700}
.way{position:absolute;top:1135px;width:322px}
.way svg{display:block;height:96px;margin-bottom:50px}
.way h3{font-size:33px;font-weight:700;line-height:38px;margin-bottom:14px}
.way p{font-size:20.5px;line-height:25px}
.model{position:absolute;top:1604px;left:0;width:100%;height:727px;background:var(--band)}
.model h2{text-align:center;color:#fff;font-size:40px;padding-top:96px;font-weight:700}
.model-col{position:absolute}
.model-col h3{font-size:25px;font-weight:700;margin-bottom:22px}
.model-col p{font-size:20px;line-height:25px}
.clients h2{position:absolute;top:2458px;width:100%;text-align:center;font-size:42px;font-weight:700}
.client{position:absolute;top:2590px;width:259px;height:175px;background:#e4e4e4;border:4px solid #f6f6f6;box-shadow:0 0 0 2px #c9c9c9;display:flex;align-items:center;justify-content:center}
.client span{background:#fff;padding:26px 10px;font-size:24px;font-weight:700;color:#1f2a36;width:205px;text-align:center}
.video{position:absolute;top:2900px;left:0;width:100%;height:685px;background:var(--grey-band)}
.video h2{text-align:center;font-size:44px;font-weight:700;margin-top:74px}
.video h3{text-align:center;font-size:32px;font-weight:700;margin-top:6px}
.video h3 em{font-style:normal;color:var(--red);font-size:44px}
.player{position:absolute;left:328px;top:220px;width:556px;height:354px;background:#000;border:4px solid #b0b0b0}
.player .bar{position:absolute;left:0;right:0;bottom:0;height:34px;background:linear-gradient(#d8e4ee,#9fb1c1)}
.player .play{position:absolute;left:262px;top:132px;width:34px;height:34px;border-radius:50%;background:#444}
.brochure{position:absolute;top:3655px;width:100%;text-align:center;font-size:40px;font-weight:700}
.brochure span{color:var(--red)}
.split{position:absolute;top:3805px;left:0;width:100%;height:717px;display:flex}
.split-photo{width:606px;height:100%;background:linear-gradient(120deg,#f4f4f4,#9aa6b4 60%,#d9c7b8)}
.split-panel{flex:1;background:var(--steel);color:#fff;text-align:center;padding-top:130px}
.split-panel h2{font-size:40px;line-height:50px;font-weight:700;width:400px;margin:0 auto}
.btn-outline{display:inline-block;margin-top:80px;width:240px;height:70px;line-height:66px;border:2px solid #fff;font-size:22px}
.footer{position:absolute;top:4522px;left:0;width:100%;height:215px;background:var(--footer);font-size:19px;line-height:31px}
.footer .copy{position:absolute;left:40px;top:60px;width:540px}
.footer .links{position:absolute;left:640px;top:60px}
</style>
</head>
<body>
<nav class="nav">
  <a class="active">HOME</a><a>OUR INCENTIVES</a><a>SAMPLES</a><a>HOW IT WORKS</a><a>TESTIMONIALS</a><a>FAQ</a><a>CONTACT</a><a class="login">LOG IN</a>
</nav>
<header class="header">
  <div class="logo"><span class="logo-dot"></span><span class="logo-name">BLPW</span></div>
  <div class="phones">
    <svg width="28" height="54" viewBox="0 0 28 54"><rect x="2" y="2" width="24" height="50" rx="4" fill="none" stroke="#111" stroke-width="3"/><rect x="6" y="8" width="16" height="24" fill="#111"/><circle cx="14" cy="44" r="3" fill="#111"/></svg>
    <p>USA Office: 555-014-2159<br>International: 1-800-555-0136</p>
  </div>
  <div class="offer">Unlimited Incentives<br>For $99 Monthly - No Contracts<br>30 Day Risk Free Trial<strong>SIGN UP RIGHT NOW</strong></div>
</header>
<section class="hero">
  <div class="hero-photo" role="img" aria-label="Businessman leaping to grab a rising red growth arrow against a pale concrete wall"></div>
  <h1>Give Away<br>Unlimited Incentives<br>To Your Customers</h1>
  <a class="btn-red">LEARN MORE</a>
</section>
<section class="ways">
  <h2>Three Easy Ways!</h2>
  <div class="way" style="left:41px">
    <svg viewBox="0 0 80 70" width="110"><rect x="18" y="4" width="44" height="18" fill="#333"/><rect x="4" y="22" width="72" height="32" rx="5" fill="#333"/><rect x="18" y="44" width="44" height="22" fill="#fff" stroke="#333" stroke-width="3"/></svg>
    <h3>PRINT</h3>
    <p>Download PDF Certificates to print and hand them out or mail them to your customers!</p>
  </div>
  <div class="way" style="left:423px">
    <svg viewBox="0 0 80 70" width="96"><path d="M4 28 L40 4 L76 28 V66 H4Z" fill="#333"/><rect x="16" y="14" width="48" height="34" fill="#fff"/><text x="40" y="40" font-size="22" text-anchor="middle" fill="#333" font-family="Arimo,sans-serif">@</text><path d="M4 28 L40 52 L76 28 V66 H4Z" fill="#333"/></svg>
    <h3>E-MAIL</h3>
    <p>Email E-Certificates to your customers with one click!</p>
  </div>
  <div class="way" style="left:834px">
    <svg viewBox="0 0 80 80" width="96"><rect x="8" y="6" width="46" height="68" rx="6" fill="none" stroke="#333" stroke-width="4"/><path d="M40 34 a10 10 0 0 1 20 0 M34 34 a16 16 0 0 1 32 0" fill="none" stroke="#333" stroke-width="3"/><rect x="46" y="36" width="8" height="26" rx="4" fill="#333"/></svg>
    <h3>FROM YOUR<br>WEBSITE</h3>
    <p>Place our HTML banners on your homepage. Your customers click on the banner to get their Certificate. We email you their contact information - 100% Lead Generation Automation!</p>
  </div>
</section>
<section class="model">
  <h2>How BLPW Plus Into Your Business Model</h2>
  <div class="model-col" style="left:42px;top:196px;width:540px"><h3>Advertising</h3><p>Boost response rates from your existing ads by adding one extra tagline: "Call for a Free Quote and receive a Three Day Two Night Hotel Stay Certificate to Las Vegas or 50 + other popular destinations, No Purchase Necessary." Imagine how many more leads you could generate.</p></div>
  <div class="model-col" style="left:682px;top:196px;width:480px"><h3>Sales</h3><p>Now that you have generated the lead, try enticing a prospect with an upgrade and offer them Two Nights Plus Airfare if they purchase today. There are so many ways to clinch a deal by offering our incentives as a reward in your closing question.</p></div>
  <div class="model-col" style="left:42px;top:436px;width:540px"><h3>Residual Business</h3><p>Remind past clients about your products &amp; services with a 2 Night Mini of your previous business clients using a personal touch and an incentive to boot.</p></div>
  <div class="model-col" style="left:682px;top:436px;width:480px"><h3>Referrals</h3><p>Contact all of your past customers and offer a Deluxe Vacation Package to anyone who fulfills your request for a new referral. Or, at the end of your sales presentation, after you have achieved the sale, seduce new clients with a tempting perk if they send you a referral.</p></div>
</section>
<section class="clients">
  <h2>Our Clients</h2>
  <div class="client" style="left:28px"><span>Harbor Realty</span></div>
  <div class="client" style="left:319px"><span>HomeValue</span></div>
  <div class="client" style="left:609px"><span>Novaro Motors</span></div>
  <div class="client" style="left:900px"><span>Skyline TV</span></div>
</section>
<section class="video">
  <h2>Watch Video</h2>
  <h3>to Save <em>20%</em> Today</h3>
  <div class="player"><span class="play"></span><span class="bar"></span></div>
</section>
<p class="brochure">View Our <span>ONLINE BROCHURE</span></p>
<section class="split">
  <div class="split-photo" role="img" aria-label="Two business people in suits shaking hands"></div>
  <div class="split-panel">
    <h2>Know Any Businesses That Could Benefit Using Incentives To Bring In More Customers?</h2>
    <a class="btn-outline">LEARN MORE</a>
  </div>
</section>
<footer class="footer">
  <p class="copy">© 2005-2014 Bright Lane Promo Works, Inc. -<br>All Rights Reserved</p>
  <p class="links">Affiliate Program | Terms &amp; Conditions | Privacy Policy |</p>
</footer>
</body>
</html>
```